User-interface and web design for new forum-style communication platform

We developed a new forum-style communication platform specially targetting stock investors to share and discuss information on companies listed on the stock exchange.

You have complete freedom for designing the user-interface and web design. Designs should include all features listed below.

Please read the attached document for full specifications. Also attached is a mockup of the layout, but this is only directional. A mockup for the user-profile is also attached, but does not need to be designed.

This project focusses on the homepage and thread view.

The winner(s) will be asked to design the complete project. (create thread box, user profile, registering, settings...)

We are looking for a well thought out, smart design that incorporates the specifications in the attached document. Please do not hesitate to contact us if anything is not clear.

Target Market(s)

Stock investors from 25 to 60 years old (the people that are currently on investor forums)

Industry/Entity Type

Communication

Font styles to use
Sans Serif

Colors

Designer to choose colors to be used in the design.

Requirements
Must have
• Full homepage design & Thread view specified in the attached document.
Nice to have
• Create thread view
- Field for adding tags
- field for subject of the thread
- text box with basic text editing
- method for sharing media
Should not have
• Logo design.

```html
<!DOCTYPE html>
<html lang="en">
<head>
<meta charset="utf-8">
<title>Talkstock – Conversation</title>
<link rel="stylesheet" href="https://fonts.googleapis.com/css2?family=Cabin:ital,wght@0,400;0,500;0,600;0,700;1,400;1,500&display=swap">
<style>
:root{
  --ink:#2b2b2b;
  --bar:#3a3a3a;
  --text:#777;
  --muted:#a9a9a9;
  --line:#e6e6e6;
  --accent:#e8410f;
  --white:#fff;
  --soft:#f7f7f7;
  --photo-a:#d9d9d9;
  --photo-b:#4a4a4a;
}
*{box-sizing:border-box;margin:0;padding:0}
html,body{width:1200px;height:1140px;overflow:hidden}
body{position:relative;background:var(--white);font-family:'Cabin',sans-serif;color:var(--ink)}

/* header */
.topbar{position:absolute;left:0;top:0;width:1200px;height:83px;background:var(--bar)}
.brand{position:absolute;left:160px;top:27px;font-weight:700;font-size:27px;letter-spacing:1px;color:var(--white)}
.search{position:absolute;left:441px;top:27px;width:431px;height:34px;background:var(--white);border-radius:5px;border:3px solid #d4d4d4;display:flex;align-items:center;overflow:hidden}
.search svg{margin:0 10px 0 12px}
.search .query{flex:1;font-size:13px;color:#888}
.search .btn{height:100%;background:#3e3e3e;color:var(--white);font-size:14px;padding:0 14px;display:flex;align-items:center;border-left:1px solid #555}
.notify{position:absolute;left:892px;top:32px;width:36px;height:28px;background:var(--white);border-radius:2px;display:flex;align-items:center;justify-content:center}
.notify .count{position:absolute;right:-6px;bottom:-6px;background:var(--accent);color:var(--white);font-size:10px;font-weight:700;width:14px;height:14px;display:flex;align-items:center;justify-content:center}
.user-select{position:absolute;left:947px;top:28px;width:94px;height:33px;background:var(--white);border:2px solid #ccc;display:flex;align-items:center;font-size:14px;color:#999;padding-left:10px}
.user-select .caret{position:absolute;right:0;top:0;width:20px;height:100%;background:#555;display:flex;align-items:center;justify-content:center}

/* main column */
.main{position:absolute;left:160px;top:114px;width:627px}
.crumbs{height:28px;border:1px solid var(--line);font-size:12px;display:flex;align-items:center;padding-left:9px;color:var(--ink)}
.crumbs a{color:var(--accent);text-decoration:none}
.crumbs .sep{color:var(--muted);margin:0 3px;font-size:10px}
.tabs{margin-top:18px;height:40px;background:var(--soft);border:1px solid var(--line);display:flex;align-items:center;position:relative}
.tab{height:100%;display:flex;align-items:center;padding:0 19px;font-size:16px;color:#888;border-right:1px solid var(--line)}
.tab.active{background:var(--white);color:var(--ink);position:relative}
.tab.active::after{content:"";position:absolute;left:50%;bottom:-6px;width:10px;height:10px;background:var(--white);border-right:1px solid var(--line);border-bottom:1px solid var(--line);transform:translateX(-50%) rotate(45deg)}
.tab.plain{border-right:none}
.create{position:absolute;right:10px;top:8px;background:var(--bar);color:var(--white);font-size:12px;height:22px;padding:0 11px;border-radius:11px;display:flex;align-items:center}

.post{display:flex;padding-bottom:36px;border-bottom:1px solid var(--line)}
.photo{width:131px;height:131px;flex:none;background:linear-gradient(135deg,var(--photo-a),var(--photo-b))}
.post-body{margin-left:18px;flex:1;position:relative}
.subject{font-weight:600;font-size:15px;color:var(--ink);margin-top:1px}
.actions{position:absolute;right:0;top:-2px;font-size:12px;color:var(--muted)}
.actions .reply{color:var(--accent)}
.actions .bar{color:#ddd;margin:0 5px}
.meta{font-size:12px;color:var(--muted);margin-top:9px}
.meta b{font-weight:500;color:var(--ink)}
.meta .bar{margin:0 5px}
.excerpt{font-size:13.5px;line-height:20.5px;color:var(--text);margin-top:11px}
.stats{display:flex;justify-content:flex-end;align-items:center;gap:6px;font-size:14px;color:var(--ink);margin-top:3px}
.stats .stat{display:flex;align-items:center;gap:6px;margin-left:18px}
.stats .more{font-style:italic;font-weight:500;font-size:13.5px;margin-left:18px}

.composer{position:relative;height:130px;border-bottom:none}
.avatar{position:absolute;left:0;top:30px;width:45px;height:45px;background:linear-gradient(135deg,#c49a7c,#6b4a3a)}
.field{position:absolute;left:64px;top:30px;width:563px;height:66px;border:1px solid #dcdcdc;font-size:13px;color:#888;padding:9px 11px}
.field::before{content:"";position:absolute;left:-6px;top:12px;width:10px;height:10px;background:var(--white);border-left:1px solid #dcdcdc;border-bottom:1px solid #dcdcdc;transform:rotate(45deg)}
.send{position:absolute;left:74px;top:106px;width:65px;height:20px;border-radius:10px;background:var(--bar);color:var(--white);font-size:13px;display:flex;align-items:center;justify-content:center}
.attach{position:absolute;right:10px;top:107px;display:flex;gap:8px}

/* sidebar */
.divider{position:absolute;left:816px;top:114px;width:1px;height:893px;background:var(--line)}
.side{position:absolute;left:844px;top:114px;width:197px}
.userbox{background:var(--bar);height:86px;padding:10px 10px}
.userbox .who{display:flex;align-items:center;gap:8px;color:var(--white);font-weight:600;font-size:16px}
.userbox .find{margin-top:9px;height:29px;background:var(--white);border-radius:2px;display:flex;align-items:center;justify-content:space-between;padding:0 3px 0 12px;font-size:13px;color:#555}
.widget h3{font-size:15px;font-weight:700;color:var(--ink);padding-bottom:8px;position:relative;letter-spacing:.2px}
.widget h3::after{content:"";position:absolute;left:0;bottom:0;width:102px;height:3px;background:#ddd}
.widget ul{list-style:none;margin-top:20px}
.widget li{font-size:13px;color:var(--text);height:30px;display:flex;align-items:flex-start}
.widget li::before{content:"";width:0;height:0;border-left:4px solid #999;border-top:4px solid transparent;border-bottom:4px solid transparent;margin:5px 8px 0 0}
.widget .all{display:inline-block;font-size:11px;color:#bbb;border-bottom:2px solid #ddd;margin-top:4px;padding-bottom:1px}
.w1{margin-top:27px}
.w2{margin-top:34px}
.w3{margin-top:35px}

/* footer */
.footer{position:absolute;left:0;top:1100px;width:1200px;height:40px;background:var(--bar);color:#ddd;font-size:11.5px;display:flex;align-items:center;justify-content:center}
</style>
</head>
<body>
<header class="topbar">
  <div class="brand">TALKSTOCK</div>
  <div class="search">
    <svg width="16" height="16" viewBox="0 0 16 16"><circle cx="9.5" cy="6.5" r="4.5" fill="none" stroke="#999" stroke-width="1.5"/><path d="M6.3 9.7 2 14" stroke="#999" stroke-width="1.8"/></svg>
    <span class="query"># acme #globex</span>
    <span class="btn">Save</span>
    <span class="btn">Clear</span>
  </div>
  <div class="notify">
    <svg width="22" height="16" viewBox="0 0 22 16"><circle cx="8" cy="4.5" r="3.5" fill="#444"/><path d="M1 15c0-4 3-6 7-6s7 2 7 6z" fill="#444"/><circle cx="15" cy="4" r="3" fill="#444"/><path d="M16 8.5c3 .3 5 2.2 5 5.5h-4.5c0-2.2-.4-4-1.5-5z" fill="#444"/></svg>
    <span class="count">3</span>
  </div>
  <div class="user-select">User
    <span class="caret"><svg width="8" height="5" viewBox="0 0 8 5"><path d="M0 0h8L4 5z" fill="#fff"/></svg></span>
  </div>
</header>

<main class="main">
  <nav class="crumbs">
    <a href="#">Home</a><span class="sep">›</span><a href="#">Conversation</a><span class="sep">›</span><a href="#">Public</a><span class="sep">›</span>&nbsp;# acme #globex
  </nav>
  <div class="tabs">
    <span class="tab active">Public</span>
    <span class="tab">Following</span>
    <span class="tab plain">Contacts</span>
    <span class="create">Create thread</span>
  </div>

  <article class="post" style="margin-top:29px">
    <div class="photo" role="img" aria-label="Black and white photo of the thread author seated in an armchair"></div>
    <div class="post-body">
      <h2 class="subject">LOREM IPSUM SUBJECT</h2>
      <div class="actions"><span class="reply">Reply</span><span class="bar">|</span>Share<span class="bar">|</span>Favourite</div>
      <p class="meta"><b>By:</b> Martin Hale<span class="bar">|</span>Jan 01, 2014<span class="bar">|</span>15:32</p>
      <p class="excerpt">Lorem Ipsum is simply dummy text of the printing and typesetting industry. Lorem Ipsum has been the industry standard dummy text ever since 1500s, when an unknown printer .</p>
      <div class="stats">
        <span class="stat">12 <svg width="10" height="9" viewBox="0 0 10 9"><path d="M8 0v5H2" fill="none" stroke="#bbb" stroke-width="1.4"/><path d="M3.5 2.5 1 5l2.5 2.5" fill="none" stroke="#bbb" stroke-width="1.4"/></svg></span>
        <span class="stat">250 <svg width="14" height="9" viewBox="0 0 14 9"><path d="M1 4.5C3 1 11 1 13 4.5 11 8 3 8 1 4.5z" fill="none" stroke="#bbb" stroke-width="1.2"/><circle cx="7" cy="4.5" r="2" fill="#bbb"/></svg></span>
        <span class="more">[ Read more ]</span>
      </div>
    </div>
  </article>

  <section class="composer">
    <div class="avatar" role="img" aria-label="Profile photo of the signed-in user"></div>
    <div class="field">Type your reply here...</div>
    <span class="send">send</span>
    <div class="attach">
      <svg width="12" height="14" viewBox="0 0 12 14"><path d="M1 1h7l3 3v9H1z" fill="none" stroke="#999" stroke-width="1.2"/><path d="M4 10c1-3 2-5 2-6s-1 0 0 2 2 3 3 3-3 0-5 1z" fill="none" stroke="#999" stroke-width=".8"/></svg>
      <svg width="13" height="14" viewBox="0 0 13 14"><rect x="1" y="1" width="11" height="12" fill="none" stroke="#999" stroke-width="1.2"/><path d="M4 1v12M9 1v12M1 5h3M1 9h3M9 5h3M9 9h3" stroke="#999"/></svg>
      <svg width="16" height="14" viewBox="0 0 16 14"><path d="M1 4h3l2-2h4l2 2h3v9H1z" fill="#999"/><circle cx="8" cy="8" r="3" fill="#fff"/><circle cx="8" cy="8" r="1.8" fill="#999"/></svg>
    </div>
  </section>

  <article class="post" style="margin-top:5px">
    <div class="photo" role="img" aria-label="Black and white photo of the thread author seated in an armchair"></div>
    <div class="post-body">
      <h2 class="subject">LOREM IPSUM SUBJECT</h2>
      <div class="actions"><span class="reply">Reply</span><span class="bar">|</span>Share<span class="bar">|</span>Favourite</div>
      <p class="meta"><b>By:</b> Martin Hale<span class="bar">|</span>Jan 01, 2014<span class="bar">|</span>15:32</p>
      <p class="excerpt">Lorem Ipsum is simply dummy text of the printing and typesetting industry. Lorem Ipsum has been the industry standard dummy text ever since 1500s, when an unknown printer .</p>
      <div class="stats">
        <span class="stat">12 <svg width="10" height="9" viewBox="0 0 10 9"><path d="M8 0v5H2" fill="none" stroke="#bbb" stroke-width="1.4"/><path d="M3.5 2.5 1 5l2.5 2.5" fill="none" stroke="#bbb" stroke-width="1.4"/></svg></span>
        <span class="stat">250 <svg width="14" height="9" viewBox="0 0 14 9"><path d="M1 4.5C3 1 11 1 13 4.5 11 8 3 8 1 4.5z" fill="none" stroke="#bbb" stroke-width="1.2"/><circle cx="7" cy="4.5" r="2" fill="#bbb"/></svg></span>
        <span class="more">[ Read more ]</span>
      </div>
    </div>
  </article>

  <article class="post" style="margin-top:38px">
    <div class="photo" role="img" aria-label="Black and white photo of the thread author seated in an armchair"></div>
    <div class="post-body">
      <h2 class="subject">LOREM IPSUM SUBJECT</h2>
      <div class="actions"><span class="reply">Reply</span><span class="bar">|</span>Share<span class="bar">|</span>Favourite</div>
      <p class="meta"><b>By:</b> Martin Hale<span class="bar">|</span>Jan 01, 2014<span class="bar">|</span>15:32</p>
      <p class="excerpt">Lorem Ipsum is simply dummy text of the printing and typesetting industry. Lorem Ipsum has been the industry standard dummy text ever since 1500s, when an unknown printer .</p>
      <div class="stats">
        <span class="stat">12 <svg width="10" height="9" viewBox="0 0 10 9"><path d="M8 0v5H2" fill="none" stroke="#bbb" stroke-width="1.4"/><path d="M3.5 2.5 1 5l2.5 2.5" fill="none" stroke="#bbb" stroke-width="1.4"/></svg></span>
        <span class="stat">250 <svg width="14" height="9" viewBox="0 0 14 9"><path d="M1 4.5C3 1 11 1 13 4.5 11 8 3 8 1 4.5z" fill="none" stroke="#bbb" stroke-width="1.2"/><circle cx="7" cy="4.5" r="2" fill="#bbb"/></svg></span>
        <span class="more">[ Read more ]</span>
      </div>
    </div>
  </article>
</main>

<div class="divider"></div>

<aside class="side">
  <div class="userbox">
    <div class="who">
      <svg width="24" height="24" viewBox="0 0 24 24"><circle cx="12" cy="12" r="11" fill="none" stroke="#fff" stroke-width="1.6"/><circle cx="12" cy="9.5" r="4" fill="#fff"/><path d="M5 19c1.5-3.5 4-5 7-5s5.5 1.5 7 5" fill="#fff"/></svg>
      User
    </div>
    <div class="find">Search
      <svg width="23" height="23" viewBox="0 0 23 23"><circle cx="11.5" cy="11.5" r="11.5" fill="#333"/><circle cx="10.5" cy="10.5" r="4" fill="none" stroke="#fff" stroke-width="1.6"/><path d="M13.5 13.5 17 17" stroke="#fff" stroke-width="1.8"/></svg>
    </div>
  </div>

  <section class="widget w1">
    <h3>SAVE FILTERS</h3>
    <ul><li>Item One</li><li>Item Two</li><li>Item Three</li><li>Item Four</li><li>Item Five</li><li>Item Six</li></ul>
    <span class="all">View All</span>
  </section>

  <section class="widget w2">
    <h3>POPOLAR TAG</h3>
    <ul><li>Item One</li><li>Item Two</li><li>Item Three</li><li>Item Four</li><li>Item Five</li><li>Item Six</li></ul>
    <span class="all">View All</span>
  </section>

  <section class="widget w3">
    <h3>POPULAR CONTRIBUTORS</h3>
    <ul><li>Item One</li><li>Item Two</li><li>Item Three</li><li>Item Four</li><li>Item Five</li><li>Item Six</li></ul>
    <span class="all">View All</span>
  </section>
</aside>

<footer class="footer">© Copyrights 2014 Talkstock. All Rights Reserved</footer>
</body>
</html>
```